Forget what you know about corporate well

I need a one-page flies used for print, to embedding in a website, all social media platforms and email.

Target Market(s)

Business

Industry/Entity Type

Health And Wellness

Font styles to use
Serif
Script
Other font styles liked:
• I would like the designers opinion on the font

Colors

Designer to choose colors to be used in the design.

Requirements
Must have
• This is the wording:
• Did you know that 75% of healthcare costs are incurred by preventable diseases? Cardiovascular disease, cancer, and diabetes are the three major causes of rising health care plans and are all preventable.
• Milo and his team have spent decades learning how to increase productivity, reduce absenteeism, and increase employee engagement, all leading to lowering healthcare costs. Together, they have developed a system created to target the masses all while addressing individual needs. Their corporate training challenges helps to engrain positive habits through a carefully curated accountability and reward system.
• How it works:
• Step 1 – evaluate the needs of your business;
• Step 2 – set up individualized workshops based on highest needs;
• Step 3 – create a customized corporate training challenge.
• Why Milo?
• Milo excels at motivational speaking. He is an author, a nutritionist and a professional athlete with a master’s degree in clinical nutrition. He is a teacher of corporate wellness at Fernhollow College and a health coach. Milo has been featured in national magazines, podcasts, and popular fitness websites. Milo’s own health issues put him on a quest to heal himself and others. With twenty-five years of experience and a passion for wellness, he can provide your company with an unforgettable experience.
Nice to have
• I will not give my opinion, I believe that is an insult to the designer. All of the verbiage is above and I attached a plethora of pictures.
Should not have
• No opinion

```html
<!DOCTYPE html>
<html lang="en">
<head>
<meta charset="utf-8">
<title>Steadfast Wellness – Corporate Wellness</title>
<link href="https://fonts.googleapis.com/css2?family=Jost:wght@300;400;500;700&display=swap" rel="stylesheet">
<style>
  :root {
    --green: #41a84a;
    --green-panel: rgba(74, 172, 74, 0.86);
    --green-text: #2b8a33;
    --white: #ffffff;
    --brick-light: #c8735a;
    --brick-mid: #ad5a44;
    --brick-dark: #84402f;
    --mural: #e6ddd6;
    --figure: #2a2426;
    --photo-cool: #5f7282;
    --photo-warm: #b9aea5;
  }
  * { margin: 0; padding: 0; box-sizing: border-box; }
  html, body { width: 927px; height: 1200px; overflow: hidden; background: var(--white); }
  body { font-family: "Jost", "Futura", sans-serif; font-weight: 300; position: relative; }

  .hero {
    position: absolute; left: 0; top: 0; width: 927px; height: 607px;
    background:
      radial-gradient(ellipse 110px 230px at 190px 420px, rgba(42,36,38,0.85) 0%, rgba(42,36,38,0.55) 55%, rgba(42,36,38,0) 100%),
      radial-gradient(ellipse 260px 130px at 220px 70px, rgba(230,221,214,0.7) 0%, rgba(230,221,214,0.25) 55%, rgba(230,221,214,0) 100%),
      linear-gradient(180deg, rgba(0,0,0,0) 70%, rgba(120,60,45,0.35) 100%),
      linear-gradient(120deg, var(--brick-light) 0%, var(--brick-mid) 50%, var(--brick-dark) 100%);
  }
  .intro-panel {
    position: absolute; left: 464px; top: 0; width: 312px; height: 482px;
    background: var(--green-panel); color: var(--white); text-align: center;
  }
  .brand-mark {
    position: absolute; left: 136px; top: 30px; width: 40px; height: 40px;
    border-radius: 50%; background: var(--white);
  }
  .brand-name {
    position: absolute; left: 0; right: 0; top: 101px;
    font-size: 20px; font-weight: 700; letter-spacing: 0.2px;
  }
  .brand-owner {
    position: absolute; left: 0; right: 0; top: 134px;
    font-size: 20px; font-weight: 700;
  }
  .panel-rule {
    position: absolute; left: 25px; right: 25px; top: 190px; height: 2px; background: var(--white);
  }
  .intro-text {
    position: absolute; left: 26px; right: 26px; top: 205px;
    font-size: 15.6px; line-height: 21.3px;
  }

  .steps-band {
    position: absolute; left: 0; top: 618px; width: 927px; height: 110px;
    background: var(--green); color: var(--white);
  }
  .steps-title {
    position: absolute; left: 56px; top: 22px; font-size: 55px; font-weight: 300; letter-spacing: -0.8px; white-space: nowrap;
  }
  .steps-divider {
    position: absolute; left: 374px; top: 24px; width: 2px; height: 62px; background: var(--white);
  }
  .steps-list {
    position: absolute; left: 404px; top: 20px; list-style: none;
    font-size: 18.5px; line-height: 24.5px; white-space: nowrap;
  }

  .bio-photo {
    position: absolute; left: 0; top: 739px; width: 302px; height: 298px;
    background:
      radial-gradient(ellipse 110px 150px at 150px 190px, rgba(40,58,84,0.85) 0%, rgba(40,58,84,0) 100%),
      linear-gradient(90deg, var(--photo-cool) 0%, var(--photo-warm) 60%, #d9d6d2 100%);
    box-shadow: 3px 4px 8px rgba(0,0,0,0.35);
  }
  .bio-title {
    position: absolute; left: 458px; width: 322px; top: 757px;
    text-align: center; color: var(--green-text); font-size: 37px; font-weight: 400; white-space: nowrap;
  }
  .bio-rule {
    position: absolute; left: 474px; width: 290px; top: 814px; border-top: 2px dotted var(--green-text);
  }
  .bio-text {
    position: absolute; left: 365px; width: 510px; top: 830px;
    color: var(--green-text); font-size: 15.8px; font-weight: 400; line-height: 27.3px;
  }

  .fact-band {
    position: absolute; left: 0; top: 1048px; width: 927px; height: 152px;
    background: var(--green); color: var(--white);
  }
  .fact-icon {
    position: absolute; left: 46px; top: 43px; width: 74px; height: 60px;
  }
  .fact-divider {
    position: absolute; left: 143px; top: 48px; width: 2px; height: 58px; background: var(--white);
  }
  .fact-text {
    position: absolute; left: 163px; top: 43px; width: 712px;
    font-size: 15.8px; line-height: 22px;
  }
  .fact-text strong { font-weight: 700; font-size: 16px; letter-spacing: 0.1px; }
</style>
</head>
<body>

<section class="hero" role="img" aria-label="Photo of Milo smiling in a black t-shirt in front of a red brick wall with a painted mural"></section>

<aside class="intro-panel">
  <span class="brand-mark"></span>
  <div class="brand-name">Steadfast Wellness</div>
  <div class="brand-owner">Milo T. Varden</div>
  <div class="panel-rule"></div>
  <p class="intro-text">Milo and his team have spent decades learning how to increase productivity, reduce absenteeism, and increase employee engagement, all leading to lowering healthcare costs. Together, they have developed a system created to target the masses all while addressing individual needs. Their corporate training challenges helps to ingrain positive habits through a carefully curated accountability and reward system.</p>
</aside>

<section class="steps-band">
  <h2 class="steps-title">How It Works</h2>
  <div class="steps-divider"></div>
  <ul class="steps-list">
    <li>Evaluate the needs of your business</li>
    <li>Set-up individualized workshops based on highest needs</li>
    <li>Create a customized corporate training challenge</li>
  </ul>
</section>

<div class="bio-photo" role="img" aria-label="Portrait of Milo with arms crossed wearing a striped sweater outdoors"></div>
<h2 class="bio-title">Milo’s Experience</h2>
<div class="bio-rule"></div>
<p class="bio-text">Milo excels at motivational speaking. He is an author, a nutritionist and a professional athlete with a master’s degree in clinical nutrition. He is a teacher of corporate wellness at Fernhollow College and a health coach. Milo has been featured in national magazines, pod-casts, and popular fitness websites. Milo’s own health issues put him on a quest to heal himself and others. With twenty-five years of experience and a passion for wellness, he can provide your company with an unforgettable experience.</p>

<section class="fact-band">
  <svg class="fact-icon" viewBox="0 0 74 60" role="img" aria-label="Did you know illustration of a head with a brain">
    <rect x="0" y="0" width="74" height="60" rx="10" fill="rgba(255,255,255,0.28)"/>
  </svg>
  <div class="fact-divider"></div>
  <p class="fact-text"><strong>Did you know that 75% of healthcare costs are incurred by preventable diseases?</strong><br>Cardiovascular disease, cancer, and diabetes are the three major causes of rising health care plans and are all preventable.</p>
</section>

</body>
</html>
```